beauty salon application for consumer

- Find your favorite beauty salons and spas or discover new places next to you with geolocation;
- Filter your search by price, distance, category and type of service;
- Never worry again about having to schedule during your work hours or about not having your calls answered when you want to book an appointment;
- Mark salons as favorites and be the first to be informed of exclusive discounts;
- Don’t ever forget your appointments with Glow Nook’s notifications;
- Compare prices, places and services freely, in a quick and practical way;
- Share reviews about services and places you go with other users and read their opinions;
- USER-FRIENDLY INTERFACE
- GALLERY
- OFFERS

similar interface with application name "primlane"

Industry/Entity Type

Beauty Salon

Font styles to use
Decorative
Script

Colors

Designer to choose colors to be used in the design.

Requirements
Must have
• Please have a look into these applications:
• 1- https://apps.example-store.test/gb/app/primlane/id502918377/?pid=corvella&c=footer-link
• 2- https://apps.example-store.test/us/app/fizz-ltd-book-curl-set-glam-nail-services/id6093817245
• 3- https://market.sample-apps.test/store/apps/details?id=com.lumiparlour.user&hl=en
• 4- https://apps.example-store.test/app/id361720498?mt=8
Nice to have
• Nice to give me a clear screenshots for main function of the application ,please see the above applications before giving me a design .

```html
<!DOCTYPE html>
<html lang="en">
<head>
<meta charset="utf-8">
<title>Lumora Apps – Navigation Drawer</title>
<link href="https://fonts.googleapis.com/css2?family=Open+Sans:wght@400;600&display=swap" rel="stylesheet">
<style>
  :root {
    --header-bg: #646464;
    --drawer-bg: #343a42;
    --backdrop: #c7c7c7;
    --avatar: #c4c4c4;
    --search-bg: #44525d;
    --text-light: #f2f2f2;
    --text-muted: #cfd4d8;
    --icon: #d9dde0;
    --badge: #e0342a;
  }
  * { box-sizing: border-box; margin: 0; padding: 0; }
  html, body { width: 675px; height: 1200px; overflow: hidden; }
  body { font-family: "Open Sans", Arial, sans-serif; background: var(--backdrop); position: relative; }

  .drawer { position: absolute; left: 0; top: 0; width: 504px; height: 1200px; background: var(--drawer-bg); }

  .profile { height: 338px; background: var(--header-bg); position: relative; }
  .profile__avatar { position: absolute; left: 194px; top: 84px; width: 112px; height: 112px; border-radius: 50%; background: var(--avatar); }
  .profile__name { position: absolute; left: 0; width: 100%; top: 212px; text-align: center; color: var(--text-light); font-size: 31px; font-weight: 400; }

  .search { position: absolute; left: 22px; top: 402px; width: 454px; height: 50px; border-radius: 25px; background: var(--search-bg); display: flex; align-items: center; padding-left: 30px; }
  .search svg { width: 24px; height: 24px; }
  .search__placeholder { margin-left: 16px; color: var(--text-muted); font-size: 22px; }

  .menu { list-style: none; position: absolute; left: 0; top: 0; width: 100%; }
  .menu__item { position: absolute; left: 40px; display: flex; align-items: center; height: 50px; }
  .menu__icon { width: 46px; height: 46px; position: relative; }
  .menu__icon svg { width: 46px; height: 46px; }
  .menu__label { margin-left: 36px; color: var(--text-light); font-size: 27px; letter-spacing: 0.3px; }
  .badge { position: absolute; left: 30px; top: -8px; width: 24px; height: 24px; border-radius: 50%; background: var(--badge); color: #fff; font-size: 15px; line-height: 24px; text-align: center; }
</style>
</head>
<body>
  <nav class="drawer">
    <header class="profile">
      <div class="profile__avatar"></div>
      <p class="profile__name">Lumora Apps</p>
    </header>

    <div class="search">
      <svg viewBox="0 0 24 24" fill="none" stroke="#e6e9eb" stroke-width="2.4" stroke-linecap="round"><circle cx="10" cy="10" r="7"/><line x1="15.5" y1="15.5" x2="22" y2="22"/></svg>
      <span class="search__placeholder">Search ...</span>
    </div>

    <ul class="menu">
      <li class="menu__item" style="top:562px">
        <span class="menu__icon"><svg viewBox="0 0 46 46" fill="none" stroke="var(--icon)" stroke-width="2" stroke-linejoin="round"><path d="M6 22 L23 7 L40 22"/><path d="M11 18 V39 H35 V18"/><path d="M19 39 V28 H27 V39"/></svg></span>
        <span class="menu__label">HOME</span>
      </li>
      <li class="menu__item" style="top:652px">
        <span class="menu__icon"><svg viewBox="0 0 46 46" fill="none" stroke="var(--icon)" stroke-width="2" stroke-linejoin="round" stroke-linecap="round"><path d="M7 26 V39 H39 V26"/><path d="M7 26 H16 L18 31 H28 L30 26 H39"/><path d="M23 10 V24"/><path d="M17 18 L23 24 L29 18"/></svg><span class="badge">5</span></span>
        <span class="menu__label">BOOKINGS</span>
      </li>
      <li class="menu__item" style="top:735px">
        <span class="menu__icon"><svg viewBox="0 0 46 46" fill="none" stroke="var(--icon)" stroke-width="2" stroke-linejoin="round"><circle cx="23" cy="23" r="6"/><path d="M20 6 H26 L27 11 L31 13 L36 10 L40 14 L37 19 L39 23 L37 27 L40 32 L36 36 L31 33 L27 35 L26 40 H20 L19 35 L15 33 L10 36 L6 32 L9 27 L7 23 L9 19 L6 14 L10 10 L15 13 L19 11 Z"/></svg></span>
        <span class="menu__label">SETTINGS</span>
      </li>
      <li class="menu__item" style="top:828px">
        <span class="menu__icon"><svg viewBox="0 0 46 46" fill="none" stroke="var(--icon)" stroke-width="2" stroke-linejoin="round"><path d="M6 9 H40 V32 H20 L13 38 V32 H6 Z"/><circle cx="15" cy="21" r="1.3" fill="var(--icon)"/><circle cx="23" cy="21" r="1.3" fill="var(--icon)"/><circle cx="31" cy="21" r="1.3" fill="var(--icon)"/></svg></span>
        <span class="menu__label">NOTIFICATION</span>
      </li>
      <li class="menu__item" style="top:920px">
        <span class="menu__icon"><svg viewBox="0 0 46 46" fill="none" stroke="var(--icon)" stroke-width="2" stroke-linejoin="round" stroke-linecap="round"><path d="M14 14 V7 H37 V39 H14 V32"/><path d="M8 23 H27"/><path d="M21 17 L27 23 L21 29"/></svg></span>
        <span class="menu__label">SIGN OUT</span>
      </li>
    </ul>
  </nav>
</body>
</html>
```